Brightway home services

Home maintenance. Electrical services plumbing services appliance repairs. Garden services. Landscaping. Faulty sockets and lights and fitting leaking taps and pipes all appliances repaired garden fencing and gates and landscaping. tel 07482913606

Industry/Entity Type

Appliance

```html
<!DOCTYPE html>
<html lang="en">
<head>
<meta charset="utf-8">
<title>Brightway home services – Home Maintenance flyer</title>
<link rel="stylesheet" href="https://fonts.googleapis.com/css2?family=Open+Sans:wght@600;700&family=Roboto+Condensed:wght@700&display=swap">
<style>
  :root {
    --backdrop: #8c8c8c;
    --flyer-blue: #0e587b;
    --brand-orange: #f2901c;
    --copy-orange: #e9a23b;
    --service-blue: #144f86;
    --white: #ffffff;
  }
  * { margin: 0; padding: 0; box-sizing: border-box; }
  html, body {
    width: 1200px; height: 900px; overflow: hidden;
    background: var(--backdrop);
  }
  .flyer {
    position: absolute; left: 300px; top: 26px;
    width: 600px; height: 848px;
    background: var(--flyer-blue);
    overflow: hidden;
    box-shadow: 0 6px 18px rgba(0,0,0,.25);
  }
  .flyer__art { position: absolute; inset: 0; width: 600px; height: 848px; }
  .flyer__title {
    position: absolute; left: 48px; top: 44px;
    font-family: "Open Sans", Arial, sans-serif;
    font-weight: 700; font-size: 42px; letter-spacing: .5px;
    color: var(--white);
  }
  .flyer__summary {
    position: absolute; left: 64px; top: 128px; width: 310px;
    font-family: "Roboto Condensed", "Arial Narrow", sans-serif;
    font-weight: 700; font-size: 16px; line-height: 1.62;
    letter-spacing: .6px; text-transform: uppercase;
    color: var(--copy-orange);
  }
  .service-list {
    font-family: "Roboto Condensed", "Arial Narrow", sans-serif;
    font-weight: 700; font-size: 17px; letter-spacing: .4px;
    fill: var(--service-blue);
  }
  .contact {
    position: absolute; left: 62px; top: 690px;
    font-family: "Open Sans", Arial, sans-serif;
  }
  .contact__label { font-weight: 600; font-size: 24px; color: var(--white); letter-spacing: 1px; }
  .contact__phone { font-weight: 700; font-size: 31px; color: var(--brand-orange); line-height: 1.1; }
</style>
</head>
<body>
  <article class="flyer" aria-label="Brightway home services flyer">
    <svg class="flyer__art" viewBox="0 0 600 848" xmlns="http://www.w3.org/2000/svg">
      <defs>
        <linearGradient id="garden-tone" x1="0" y1="0" x2="0" y2="1">
          <stop offset="0" stop-color="#3f6b2c"/>
          <stop offset=".5" stop-color="#b45a6e"/>
          <stop offset="1" stop-color="#5e9a35"/>
        </linearGradient>
        <linearGradient id="appliance-tone" x1="0" y1="0" x2="1" y2="1">
          <stop offset="0" stop-color="#f1f1ef"/>
          <stop offset="1" stop-color="#cfd2d2"/>
        </linearGradient>
        <linearGradient id="plumbing-tone" x1="0" y1="0" x2="1" y2="1">
          <stop offset="0" stop-color="#d9dcdf"/>
          <stop offset=".6" stop-color="#b98a74"/>
          <stop offset="1" stop-color="#eceae6"/>
        </linearGradient>
        <linearGradient id="socket-tone" x1="0" y1="0" x2="1" y2="1">
          <stop offset="0" stop-color="#cdb8a2"/>
          <stop offset="1" stop-color="#e6dccf"/>
        </linearGradient>
      </defs>

      <g class="collage" transform="translate(-40 470) rotate(-24)" stroke="#ffffff" stroke-width="3">
        <rect class="collage__accent" x="-120" y="172" width="120" height="43" fill="var(--brand-orange)" stroke="none"/>
        <rect class="collage__tile" role="img" aria-label="Photo of a lawn mower cutting grass beside flower beds"
              x="-120" y="0" width="350" height="170" fill="url(#garden-tone)"/>
        <rect class="collage__tile" role="img" aria-label="Photo of hands repairing a white kitchen appliance"
              x="230" y="0" width="190" height="170" fill="url(#appliance-tone)"/>
        <rect class="collage__panel" x="420" y="0" width="400" height="170" fill="var(--brand-orange)"/>
        <rect class="collage__tile" role="img" aria-label="Photo of a plumber tightening pipes with a wrench"
              x="280" y="170" width="260" height="160" fill="url(#plumbing-tone)"/>
        <rect class="collage__accent" x="540" y="170" width="280" height="160" fill="var(--brand-orange)"/>
        <rect class="collage__tile" role="img" aria-label="Photo of an electrician fitting a wall socket with a screwdriver"
              x="280" y="330" width="540" height="400" fill="url(#socket-tone)"/>

        <g class="service-list" stroke="none">
          <text x="440" y="34">ELECTRICAL SERVICES</text>
          <text x="440" y="58">PLUMBING SERVICES</text>
          <text x="440" y="82">APPLIANCE REPAIRS</text>
          <text x="440" y="106">GARDEN SERVICES</text>
          <text x="440" y="130">LANDSCAPING</text>
        </g>
      </g>
    </svg>

    <h1 class="flyer__title">HOME MAINTENANCE</h1>
    <p class="flyer__summary">Faulty sockets and lights and fitting leaking taps and pipes all appliances repaired garden fencing and gates and landscaping.</p>

    <div class="contact">
      <p class="contact__label">CALL</p>
      <p class="contact__phone">07482913606</p>
    </div>
  </article>
</body>
</html>
```